Legal Service Estimated Retainer and Average Case Value

We need an 11x14 flyer that contains the standard retainers and average cost be case, both provided in documents, for each case type we handle. We need the information displayed, preferably in a way that makes the information readable but less troubling to a client shocked at price of litigation. We need one sheet with the retainers and average case value merged into one table.

Target Market(s)

Potential Clients

Font styles to use
Serif
Sans Serif

```html
<!DOCTYPE html>
<html lang="en">
<head>
<meta charset="utf-8">
<title>Hollander Law Office – Fees and Retainers</title>
<link rel="stylesheet" href="https://fonts.googleapis.com/css2?family=Cinzel:wght@500;600;700&display=swap">
<style>
  :root {
    --navy: #14204a;
    --footer: #0b1541;
    --band-light: #cfcfcd;
    --band-dark: #3f3838;
    --row-tint: rgba(255,255,255,0.88);
    --row-alt: rgba(233,236,242,0.88);
    --rule: rgba(20,32,74,0.18);
    --paper: #ffffff;
    --white: #ffffff;
  }
  * { margin: 0; padding: 0; box-sizing: border-box; }
  html, body { width: 975px; height: 1200px; overflow: hidden; background: var(--paper); }
  .flyer {
    position: relative;
    width: 975px;
    height: 1200px;
    background: var(--paper);
    font-family: "Cinzel", serif;
    color: var(--navy);
    overflow: hidden;
  }
  .hero-photo {
    position: absolute;
    top: 0;
    right: 0;
    width: 560px;
    height: 1152px;
    background:
      radial-gradient(ellipse 160px 200px at 78% 22%, rgba(176,150,136,0.55), transparent 70%),
      radial-gradient(ellipse 180px 420px at 88% 62%, rgba(52,38,34,0.75), transparent 75%),
      radial-gradient(ellipse 220px 160px at 55% 90%, rgba(238,230,222,0.9), transparent 75%),
      linear-gradient(90deg, rgba(255,255,255,1) 0%, rgba(226,234,242,0.6) 30%, rgba(196,210,224,0.7) 60%, rgba(120,120,128,0.6) 100%);
  }
  .brand {
    position: absolute;
    top: 42px;
    left: 46px;
    display: flex;
    align-items: center;
    gap: 16px;
  }
  .brand-mark { width: 92px; height: 92px; background: var(--navy); }
  .brand-name { font-weight: 600; color: var(--navy); line-height: 1; }
  .brand-name .prefix { display: block; font-size: 17px; letter-spacing: 0.5px; margin-bottom: 4px; }
  .brand-name .name { display: block; font-size: 36px; letter-spacing: 0.5px; }
  .section-band {
    position: absolute;
    left: 44px;
    top: 215px;
    width: 608px;
    height: 48px;
    display: flex;
    align-items: center;
    padding-left: 18px;
    font-size: 20px;
    font-weight: 600;
    letter-spacing: 0.3px;
    background: var(--band-light);
    color: var(--navy);
  }
  .intro {
    position: absolute;
    left: 46px;
    top: 290px;
    width: 600px;
    font-size: 13.4px;
    font-weight: 600;
    line-height: 19.6px;
  }
  .fee-table {
    position: absolute;
    left: 44px;
    top: 408px;
    width: 640px;
    border-collapse: collapse;
    font-size: 13.4px;
    font-weight: 600;
    line-height: 17px;
  }
  .fee-table thead th {
    background: var(--band-dark);
    color: var(--white);
    font-size: 14px;
    font-weight: 600;
    height: 46px;
    padding: 0 14px;
    text-align: left;
    letter-spacing: 0.3px;
  }
  .fee-table thead th.amount { text-align: right; }
  .fee-table tbody td {
    height: 40px;
    padding: 0 14px;
    border-bottom: 1px solid var(--rule);
    background: var(--row-tint);
    vertical-align: middle;
  }
  .fee-table tbody tr:nth-child(even) td { background: var(--row-alt); }
  .fee-table td.amount { text-align: right; white-space: nowrap; }
  .fee-table .case { width: 330px; }
  .footer {
    position: absolute;
    left: 0;
    bottom: 0;
    width: 975px;
    height: 48px;
    background: var(--footer);
    color: var(--white);
    display: flex;
    align-items: center;
    justify-content: center;
    font-size: 16px;
    font-weight: 600;
    letter-spacing: 0.5px;
  }
</style>
</head>
<body>
<div class="flyer">
  <div class="hero-photo" role="img" aria-label="Photo of a smiling grey-haired attorney in a suit shaking hands with a client across an office desk"></div>

  <header class="brand">
    <div class="brand-mark"></div>
    <div class="brand-name">
      <span class="prefix">THE LAW OFFICE OF</span>
      <span class="name">MARCUS T HOLLANDER</span>
    </div>
  </header>

  <h2 class="section-band">Average Fee Per Case Type</h2>

  <p class="intro">In order for our clients to set expectations for legal fees, we provide the national average range of fees per case type. These are only to provide you with an understanding of what other cases have cost clients in similar cases. Please note these are not estimates nor guarantees of your own legal costs.</p>

  <table class="fee-table">
    <thead>
      <tr>
        <th class="case">Case Type</th>
        <th class="amount">Average Fee</th>
        <th class="amount">Retainer</th>
      </tr>
    </thead>
    <tbody>
      <tr><td class="case">Divorce (3301c)</td><td class="amount">$1,500 - $3,000</td><td class="amount">$2,000</td></tr>
      <tr><td class="case">Divorce (3301d)</td><td class="amount">$2,000 - $3,000</td><td class="amount">$2,500</td></tr>
      <tr><td class="case">Protection from Abuse (PFA)</td><td class="amount">$1,500 - $3,000</td><td class="amount">$2,000 Paid In Full</td></tr>
      <tr><td class="case">Support</td><td class="amount">$2,000 - $4,000</td><td class="amount">–</td></tr>
      <tr><td class="case">Custody Initial Order</td><td class="amount">$4,000 - $7,000</td><td class="amount">$3,000</td></tr>
      <tr><td class="case">Custody Contempt/Modification</td><td class="amount">$5,000 - $8,000</td><td class="amount">$3,500</td></tr>
      <tr><td class="case">Custody &amp; Support</td><td class="amount">$5,000 - $8,000</td><td class="amount">$3,000</td></tr>
      <tr><td class="case">Divorce &amp; Custody</td><td class="amount">$5,000 - $8,000</td><td class="amount">$3,500</td></tr>
      <tr><td class="case">Divorce &amp; Support</td><td class="amount">–</td><td class="amount">$3,000</td></tr>
      <tr><td class="case">Divorce &amp; Equitable Distribution</td><td class="amount">$6,000 - $10,000</td><td class="amount">$3,500</td></tr>
      <tr><td class="case">Divorce, Custody &amp; Support</td><td class="amount">$8,000 - $12,000</td><td class="amount">$3,500</td></tr>
      <tr><td class="case">Divorce, Equitable Distribution &amp; Support</td><td class="amount">$8,000 - $12,000</td><td class="amount">$3,500</td></tr>
      <tr><td class="case">Divorce, Equitable Distribution &amp; Custody</td><td class="amount">$10,000 - $15,000</td><td class="amount">$5,000</td></tr>
      <tr><td class="case">Divorce, Equitable Distribution, Custody &amp; Support</td><td class="amount">$12,000 - $15,000</td><td class="amount">$3,500</td></tr>
    </tbody>
  </table>

  <footer class="footer">WWW.HOLLANDERFAMILYLAW.COM</footer>
</div>
</body>
</html>
```